Copperline Groundworks – Website Design Brief

Web Design Brief

We are seeking a web designer to build a modern, responsive website for Copperline Groundworks, a Sydney-based earthworks and excavation company.

2. Project Goal
- Build a professional, easy-to-navigate website that:
- Showcases CGW’s capabilities and past projects
- Attracts residential and commercial developers
- Builds credibility and encourages enquiries

3. Target Audience
- Residential developers and home builders
- Commercial construction firms
- Project managers seeking reliable excavation & plant hire services

4. Services to Highlight
- Bulk Excavation
- Detailed Excavation
- Demolition
- Shoring
- Plant Hire

5. Brand Style & Tone
- Clean, bold, and modern
- Professional with a “we get the job done” attitude
- Colors: Lime Green + Concrete Grey (from logo)
- Fonts: Match the modern, rounded, bold typeface in the logo
- Imagery: Showcase big machines, on-site work, before & after shots

6. Website Pages
Recommended structure:
- Home – Quick intro, project highlights, CTA
- About Us – Team story, mission, safety focus
- Services – Separate sections for each core service
- Projects – Case studies or photo gallery
- Plant Hire – Machines available, specs/photos
- Contact – Form + map + details

7. Assets Provided
- Logo (both long + stacked formats)
- Project photos. More can be provided if required.
- Copy: To be drafted

8. Deliverables
Responsive website (desktop/mobile/tablet)
- SEO-ready structure
- CMS (WordPress) for future edits
- Google Maps integration, job enquiry form

Target Market(s)

Target Audience Residential developers and home builders Commercial construction firms Project managers seeking reliable excavation & plant hire services

Industry/Entity Type

Construction

Number of Pages Required

1 page

Requirements
Must have
• Build a professional, easy-to-navigate website that: Showcases CGW’s capabilities and past projects Attracts residential and commercial developers Builds credibility and encourages enquiries
Nice to have
• All provided in the Description
Should not have

```html
<!DOCTYPE html>
<html lang="en">
<head>
<meta charset="utf-8">
<title>Copperline Groundworks</title>
<link href="https://fonts.googleapis.com/css2?family=Audiowide&family=Roboto:wght@400;500;700&display=swap" rel="stylesheet">
<style>
:root{
  --green:#6fb52c;
  --green-dark:#5a9a1f;
  --grey:#58595b;
  --grey-light:#f3f3f3;
  --ink:#1b1b1b;
  --text:#6b6b6b;
  --footer:#161616;
  --white:#fff;
}
*{box-sizing:border-box;margin:0;padding:0}
html,body{width:1200px;height:5296px;overflow:hidden}
body{position:relative;font-family:'Roboto',Arial,sans-serif;color:var(--text);background:var(--white)}
.abs{position:absolute}
.display{font-family:'Audiowide',Arial,sans-serif;font-weight:400;text-transform:uppercase;color:var(--ink);letter-spacing:1px}
.display .accent{color:var(--green)}
.btn{position:absolute;display:flex;align-items:center;justify-content:center;gap:8px;background:var(--green);color:var(--white);font:700 14px 'Roboto',sans-serif;text-transform:uppercase;border-radius:24px}
.btn svg{width:14px;height:14px}
.photo{position:absolute}
.lorem{font-size:13.5px;line-height:26.5px;text-align:justify}

/* header */
.site-header{position:absolute;left:0;top:0;width:1200px;height:88px;background:var(--white)}
.brand{position:absolute;left:110px;top:10px;font:400 17px/22px 'Audiowide',sans-serif;color:var(--green);text-transform:uppercase}
.nav{position:absolute;left:350px;top:33px;display:flex;gap:28px;font:500 14px 'Roboto',sans-serif;color:var(--ink)}
.nav .current{color:var(--green)}
.header-cta{left:805px;top:22px;width:146px;height:45px;font-size:13px}
.call{position:absolute;left:978px;top:22px;width:222px;height:45px;display:flex;align-items:center;gap:12px}
.call-icon{width:44px;height:44px;border-radius:50%;background:var(--green);display:flex;align-items:center;justify-content:center;border:3px solid #e4f1d6}
.call small{display:block;font-size:11px;color:var(--grey)}
.call strong{display:block;font-size:16px;color:var(--ink)}

/* hero */
.hero{position:absolute;left:0;top:88px;width:1200px;height:607px;background:linear-gradient(180deg,#5e6470 0%,#7b5a3e 45%,#4a3526 100%)}
.hero-title{position:absolute;left:0;width:1200px;top:196px;text-align:center;font-size:52px;color:var(--white);letter-spacing:3px}
.hero-sub{position:absolute;left:0;width:1200px;top:268px;text-align:center;color:var(--white);font-size:16px;line-height:27px}
.hero .btn{left:505px;top:343px;width:190px;height:46px}
.watch{position:absolute;left:0;width:1200px;top:414px;text-align:center;color:var(--white);font:700 15px 'Roboto',sans-serif;text-decoration:underline;text-transform:uppercase}
.arrow-round{position:absolute;width:40px;height:40px;border-radius:50%;background:rgba(0,0,0,.55);display:flex;align-items:center;justify-content:center}

/* about */
.about-frame{left:107px;top:781px;width:337px;height:308px;border:5px solid var(--green)}
.about-photo{left:132px;top:806px;width:435px;height:441px;background:linear-gradient(160deg,#8d9299,#6b6455 60%,#4d4a45)}
.about-badge{left:395px;top:1040px;width:203px;height:207px}
.section-title{position:absolute;font-size:42px}
.about-text{position:absolute;left:653px;top:888px;width:436px}

/* services */
.services{position:absolute;left:0;top:1356px;width:1200px;height:473px;background:var(--green)}
.worker{left:880px;top:1294px;width:320px;height:350px;background:linear-gradient(180deg,#2f7fd0 0%,#e8823a 55%,#d46a23 100%);border-radius:160px 160px 0 0;opacity:.9}
.services-title{left:0;width:1200px;top:1432px;text-align:center;color:var(--white)}
.services-sub{position:absolute;left:0;width:1200px;top:1500px;text-align:center;color:var(--white);font:700 15px/24px 'Roboto',sans-serif}
.service-card{position:absolute;top:1638px;width:310px;height:248px;background:var(--white);box-shadow:0 4px 14px rgba(0,0,0,.12);border-bottom:5px solid #cfcfcf;text-align:center;padding:70px 24px 0}
.service-card.active{height:294px;border-bottom-color:var(--green)}
.service-card h3{font:700 18px 'Roboto',sans-serif;color:var(--ink);margin-bottom:14px}
.service-card p{font-size:13px;line-height:23px;color:var(--text)}
.service-card .more{display:inline-flex;align-items:center;gap:6px;margin-top:18px;font:700 14px 'Roboto',sans-serif;color:var(--green);text-decoration:underline;text-transform:uppercase}
.hex{position:absolute;top:1586px;width:92px;height:103px}
.hex svg{width:92px;height:103px}
.arrow-light{position:absolute;width:44px;height:44px;border-radius:50%;background:rgba(255,255,255,.35);display:flex;align-items:center;justify-content:center}

/* plant hire */
.plant-text{position:absolute;left:111px;top:2138px;width:437px}
.plant-frame{left:818px;top:2260px;width:288px;height:253px;background:var(--green)}
.plant-photo{left:600px;top:2038px;width:489px;height:459px;background:linear-gradient(135deg,#3b4450,#8e7a68 55%,#c9c3bc)}

/* testimonials */
.testimonials{position:absolute;left:0;top:2616px;width:1200px;height:446px;background:linear-gradient(180deg,#6e6e6e,#5a5a5a)}
.testimonials-title{left:0;width:1200px;top:2688px;text-align:center;color:var(--white)}
.quote-card{position:absolute;top:2756px;width:455px;height:209px;background:var(--white);padding:22px 28px}
.stars{color:#f2c500;font-size:15px;letter-spacing:2px}
.quote-card p{font-size:13.5px;line-height:24px;margin-top:8px}
.quote-card h4{font:700 15px 'Roboto',sans-serif;color:var(--ink);margin-top:16px}
.quote-mark{position:absolute;right:22px;bottom:16px;font:700 90px/60px Georgia,serif;color:#d9d9d9;height:44px;overflow:hidden}
.avatar{position:absolute;width:72px;height:72px;border-radius:50%;background:linear-gradient(180deg,#c9ced6,#2f3f57);border:4px solid var(--white);top:2929px}
.chev{position:absolute;top:2842px}

/* projects */
.projects-title{left:0;width:1200px;top:3135px;text-align:center}
.tile{position:absolute}
.tile-a{left:111px;top:3222px;width:608px;height:296px;background:linear-gradient(160deg,#7c8175,#5a4a3c)}
.tile-b{left:738px;top:3222px;width:349px;height:604px;background:linear-gradient(180deg,#3f6fb8 0%,#4d6a3f 40%,#9a6c48 100%)}
.tile-c{left:111px;top:3535px;width:296px;height:291px;background:linear-gradient(180deg,#6fa6e0,#b5a48e 60%,#7e6f60)}
.tile-d{left:425px;top:3535px;width:294px;height:291px;background:rgba(111,181,44,.85)}
.tile-d .inner{position:absolute;left:14px;top:14px;right:14px;bottom:14px;border:1px solid rgba(255,255,255,.8)}
.tile-e{left:111px;top:3843px;width:608px;height:294px;background:linear-gradient(180deg,#c8ccd0,#6f7a6c 60%,#4a4a47)}
.tile-f{left:738px;top:3843px;width:349px;height:294px;background:linear-gradient(180deg,#6d5034,#b88758)}
.dots{position:absolute;left:0;width:1200px;top:4172px;display:flex;justify-content:center;gap:6px}
.dots i{width:12px;height:12px;border-radius:50%;border:1.5px solid var(--grey)}
.dots i.on{background:var(--grey)}

/* contact */
.contact{position:absolute;left:0;top:4274px;width:1200px;height:613px;background:linear-gradient(180deg,#f4f4f4 0%,#f4f4f4 38%,#9eb1c6 62%,#4a5b70 100%)}
.contact-title{left:0;width:1200px;top:4340px;text-align:center}
.contact-sub{position:absolute;left:300px;width:600px;top:4402px;text-align:center;font-size:14px;line-height:25px}
.field{position:absolute;background:var(--white);border:1px solid #dcdcdc;font-size:11px;color:#8a8a8a;padding:12px 12px}
.contact .btn{position:absolute}

/* footer */
.site-footer{position:absolute;left:0;top:4887px;width:1200px;height:409px;background:var(--footer);color:var(--white)}
.foot-brand{position:absolute;left:0;width:1200px;top:4970px;text-align:center;font:400 32px 'Audiowide',sans-serif;color:var(--green);letter-spacing:2px}
.foot-nav{position:absolute;left:0;width:1200px;top:5047px;display:flex;justify-content:center;gap:34px;font:700 14px 'Roboto',sans-serif;text-transform:uppercase}
.foot-nav span.sep{color:#aaa;font-weight:400}
.info{position:absolute;top:5111px;display:flex;align-items:center;gap:16px}
.info .ic{width:62px;height:62px;border-radius:50%;background:var(--green);display:flex;align-items:center;justify-content:center;border:4px solid #2b3a1d}
.info b{display:block;font-size:14px;text-transform:uppercase;margin-bottom:6px}
.info span{font-size:13px;line-height:19px}
.foot-bar{position:absolute;left:111px;top:5232px;width:978px;display:flex;align-items:center;justify-content:space-between;font-size:13px}
.foot-bar a{color:var(--green);text-decoration:underline}
.social{display:flex;gap:8px}
.social i{width:28px;height:28px;border-radius:50%;border:1.5px solid var(--white)}
.social i.on{background:var(--green);border-color:var(--green)}
</style>
</head>
<body>

<header class="site-header">
  <div class="brand">Copperline<br>Groundworks</div>
  <nav class="nav"><span class="current">Home</span><span>About Us</span><span>Our Services</span><span>Projects</span><span>Plant Hire</span></nav>
  <a class="btn header-cta">Contact Us</a>
  <div class="call">
    <div class="call-icon"><svg width="20" height="20" viewBox="0 0 24 24" fill="#fff"><path d="M6.6 10.8a15 15 0 0 0 6.6 6.6l2.2-2.2a1 1 0 0 1 1-.25 11.4 11.4 0 0 0 3.6.57 1 1 0 0 1 1 1V20a1 1 0 0 1-1 1A17 17 0 0 1 3 4a1 1 0 0 1 1-1h3.5a1 1 0 0 1 1 1c0 1.25.2 2.45.57 3.57a1 1 0 0 1-.25 1z"/></svg></div>
    <div><small>Call Us Today</small><strong>+61 2 5550 1984</strong></div>
  </div>
</header>

<section class="hero" role="img" aria-label="Excavator digging earth on a site at dusk">
  <h1 class="display hero-title">Copperline Groundworks</h1>
  <p class="hero-sub">Lorem ipsum dolor sit amet, consectetur adipiscing elit, sed do eiusmod<br>tempor incididunt ut labore et dolore magna aliqua.</p>
  <a class="btn">Get Started <svg viewBox="0 0 16 16"><circle cx="8" cy="8" r="8" fill="#fff"/><path d="M6.5 4.5 10 8l-3.5 3.5" stroke="#6fb52c" stroke-width="2" fill="none"/></svg></a>
  <div class="watch">&#9654; Watch Our Video</div>
  <div class="arrow-round" style="left:35px;top:284px"><svg width="12" height="14" viewBox="0 0 12 14"><path d="M9 1 3 7l6 6" stroke="#fff" stroke-width="2" fill="none"/></svg></div>
  <div class="arrow-round" style="left:1125px;top:284px"><svg width="12" height="14" viewBox="0 0 12 14"><path d="m3 1 6 6-6 6" stroke="#fff" stroke-width="2" fill="none"/></svg></div>
</section>

<section class="about">
  <div class="abs about-frame"></div>
  <div class="photo about-photo" role="img" aria-label="Excavator and tipper truck at a demolition yard"></div>
  <svg class="abs about-badge" viewBox="0 0 203 207">
    <polygon points="101,0 203,60 203,207 0,207 0,60" fill="#fff"/>
    <polygon points="101,12 193,66 193,207 10,207 10,66" fill="#58595b"/>
    <text x="101" y="148" text-anchor="middle" font-family="Roboto,sans-serif" font-weight="700" font-size="74" fill="#fff">50</text>
    <text x="101" y="180" text-anchor="middle" font-family="Roboto,sans-serif" font-size="13" fill="#fff">Years Experience</text>
  </svg>
  <h2 class="display section-title" style="left:653px;top:822px">About <span class="accent">Us</span></h2>
  <p class="about-text lorem">Lorem ipsum dolor sit amet, consectetur adipiscing elit, sed do eiusmod tempor incididunt ut labore et dolore magna aliqua. Ut enim ad minim veniam, quis nostrud exercitation ullamco laboris nisi ut aliquip ex ea commodo consequat. Duis aute irure dolor in reprehenderit in voluptate velit esse cillum dolore eu fugiat nulla pariatur. Excepteur sint occaecat cupidatat non proident, sunt in culpa qui officia deserunt mollit anim id est laborum. Lorem ipsum dolor sit amet, consectetur adipiscing elit, sed do eiusmod tempor incididunt ut labore et dolore magna aliqua. Ut enim ad minim veniam, quis nostrud exercitation ullamco laboris nisi</p>
  <a class="btn" style="left:653px;top:1180px;width:183px;height:43px">Contact Us <svg viewBox="0 0 16 16"><circle cx="8" cy="8" r="8" fill="#fff"/><path d="M6.5 4.5 10 8l-3.5 3.5" stroke="#6fb52c" stroke-width="2" fill="none"/></svg></a>
</section>

<section class="services"></section>
<div class="photo worker" role="img" aria-label="Smiling site worker in hard hat and hi-vis vest giving a thumbs up"></div>
<h2 class="display section-title services-title">Our Services</h2>
<p class="services-sub">Lorem ipsum dolor sit amet, consectetur adipiscing elit, sed do eiusmod<br>et dolore magna aliqua. Ut enim ad minim veniam</p>
<div class="arrow-light" style="left:34px;top:1729px"><svg width="10" height="14" viewBox="0 0 10 14"><path d="M8 1 2 7l6 6" stroke="#fff" stroke-width="2" fill="none"/></svg></div>
<div class="arrow-light" style="left:1122px;top:1729px"><svg width="10" height="14" viewBox="0 0 10 14"><path d="m2 1 6 6-6 6" stroke="#fff" stroke-width="2" fill="none"/></svg></div>

<article class="service-card" style="left:111px"><h3>Bulk Excavation</h3><p>Lorem ipsum dolor sit amet, consectetur adipiscing elit, sed do eiusmod tempor inci didunt ut labore et dolore magna aliqua. Ut enim ad minim veniam, quis nostrud exer citation ullamco</p></article>
<article class="service-card active" style="left:444px"><h3>Detailed Excavation</h3><p>Lorem ipsum dolor sit amet, consectetur adipiscing elit, sed do eiusmod tempor inci didunt ut labore et dolore magna aliqua. Ut enim ad minim veniam, quis nostrud exer citation ullamco</p><span class="more">Learn More <svg width="14" height="14" viewBox="0 0 16 16"><circle cx="8" cy="8" r="8" fill="#6fb52c"/><path d="M6.5 4.5 10 8l-3.5 3.5" stroke="#fff" stroke-width="2" fill="none"/></svg></span></article>
<article class="service-card" style="left:777px"><h3>Demolition</h3><p>Lorem ipsum dolor sit amet, consectetur adipiscing elit, sed do eiusmod tempor inci didunt ut labore et dolore magna aliqua. Ut enim ad minim veniam, quis nostrud exer citation ullamco</p></article>

<div class="hex" style="left:220px"><svg viewBox="0 0 92 103"><polygon points="46,0 92,26 92,77 46,103 0,77 0,26" fill="#7a7b7d"/><path d="M26 66h40M30 66v-8h22v8M52 58l8-16 8 4" stroke="#fff" stroke-width="2.5" fill="none"/></svg></div>
<div class="hex" style="left:553px"><svg viewBox="0 0 92 103"><polygon points="46,0 92,26 92,77 46,103 0,77 0,26" fill="#7a7b7d"/><path d="M26 68h40M32 68l6-18 14 4M52 54l10 6v8" stroke="#fff" stroke-width="2.5" fill="none"/></svg></div>
<div class="hex" style="left:886px"><svg viewBox="0 0 92 103"><polygon points="46,0 92,26 92,77 46,103 0,77 0,26" fill="#7a7b7d"/><rect x="36" y="34" width="20" height="34" stroke="#fff" stroke-width="2.5" fill="none"/><path d="M30 70h32M40 42h12M40 50h12M40 58h12" stroke="#fff" stroke-width="2.5"/></svg></div>

<section class="plant">
  <h2 class="display section-title" style="left:111px;top:2075px">Plant <span class="accent">Hire</span></h2>
  <p class="plant-text lorem">Lorem ipsum dolor sit amet, consectetur adipiscing elit, sed do eiusmod tempor incididunt ut labore et dolore magna aliqua. Ut enim ad minim veniam, quis nostrud exercitation ullamco laboris nisi ut aliquip ex ea commodo consequat. Duis aute irure dolor in reprehenderit in voluptate velit esse cillum dolore eu fugiat nulla pariatur. Excepteur sint occaecat cupidatat non proident, sunt in culpa qui officia deserunt mollit anim id est laborum. Lorem ipsum dolor sit amet, consectetur adipiscing elit, sed do eiusmod tempor incididunt ut labore et dolore magna aliqua. Ut enim ad minim veniam, quis nostrud exercitation ullamco laboris nisi</p>
  <a class="btn" style="left:111px;top:2408px;width:158px;height:44px">Learn More <svg viewBox="0 0 16 16"><circle cx="8" cy="8" r="8" fill="#fff"/><path d="M6.5 4.5 10 8l-3.5 3.5" stroke="#6fb52c" stroke-width="2" fill="none"/></svg></a>
  <div class="abs plant-frame"></div>
  <div class="photo plant-photo" role="img" aria-label="Two hands meeting in a handshake"></div>
</section>

<section class="testimonials" role="img" aria-label="Faded office background"></section>
<h2 class="display section-title testimonials-title">What Our Clients Say</h2>
<svg class="chev" style="left:52px" width="22" height="36" viewBox="0 0 22 36"><path d="M19 2 3 18l16 16" stroke="#fff" stroke-width="3.5" fill="none"/></svg>
<svg class="chev" style="left:1126px" width="22" height="36" viewBox="0 0 22 36"><path d="m3 2 16 16L3 34" stroke="#fff" stroke-width="3.5" fill="none"/></svg>
<article class="quote-card" style="left:125px"><div class="stars">★★★★★</div><p>Lorem ipsum dolor sit amet, consectetur adipiscing elit, sed do eiusmod tempor incididunt ut labore et dolore magna minim veniam, quis nostrud aliqua.</p><h4>Priya Lal</h4><div class="quote-mark">&#8220;</div></article>
<article class="quote-card" style="left:620px"><div class="stars">★★★★★</div><p>Lorem ipsum dolor sit amet, consectetur adipiscing elit, sed do eiusmod tempor incididunt ut labore et dolore magna minim veniam, quis nostrud aliqua.</p><h4>Mark Ellis</h4><div class="quote-mark">&#8220;</div></article>
<div class="avatar" style="left:146px" role="img" aria-label="Client portrait"></div>
<div class="avatar" style="left:641px" role="img" aria-label="Client portrait"></div>

<section class="projects">
  <h2 class="display section-title projects-title">Our <span class="accent">Projects</span></h2>
  <div class="tile tile-a" role="img" aria-label="Cleared site with excavator tracks"></div>
  <div class="tile tile-b" role="img" aria-label="Excavator in a trench between trees"></div>
  <div class="tile tile-c" role="img" aria-label="Excavator demolishing a building"></div>
  <div class="tile tile-d" role="img" aria-label="Project photo with zoom overlay"><div class="inner"></div><svg class="abs" style="left:126px;top:124px" width="44" height="44" viewBox="0 0 44 44"><circle cx="18" cy="18" r="14" stroke="#fff" stroke-width="4" fill="none"/><path d="M28 28l12 12M18 11v14M11 18h14" stroke="#fff" stroke-width="4"/></svg></div>
  <div class="tile tile-e" role="img" aria-label="Trucks and drill rig on a misty site"></div>
  <div class="tile tile-f" role="img" aria-label="Timber shoring wall along an excavation"></div>
  <div class="dots"><i></i><i class="on"></i><i></i></div>
</section>

<section class="contact" role="img" aria-label="City skyline at dusk"></section>
<h2 class="display section-title contact-title">Contact <span class="accent">Us</span></h2>
<p class="contact-sub">Lorem ipsum dolor sit amet, consectetur adipiscing elit, sed do eiusmod tempor incididunt ut labore et dolore magna aliqua. Ut enim ad minim veniam,</p>
<div class="field" style="left:216px;top:4486px;width:378px;height:43px">&#9786; First Name</div>
<div class="field" style="left:612px;top:4486px;width:372px;height:43px">&#9786; Last Name</div>
<div class="field" style="left:216px;top:4544px;width:378px;height:43px">&#9993; Email Address</div>
<div class="field" style="left:612px;top:4544px;width:372px;height:43px">&#9990; Phone Number</div>
<div class="field" style="left:216px;top:4601px;width:768px;height:93px">&#9998; Message</div>
<a class="btn" style="left:522px;top:4737px;width:156px;height:45px">Submit Now</a>

<footer class="site-footer"></footer>
<div class="foot-brand">COPPERLINEGROUNDWORKS</div>
<nav class="foot-nav"><span>Home</span><span class="sep">/</span><span>About Us</span><span class="sep">/</span><span>Our Services</span><span class="sep">/</span><span>Testimonials</span><span class="sep">/</span><span>Contact Us</span></nav>
<div class="info" style="left:115px"><div class="ic"><svg width="24" height="24" viewBox="0 0 24 24" fill="#fff"><path d="M6.6 10.8a15 15 0 0 0 6.6 6.6l2.2-2.2a1 1 0 0 1 1-.25 11.4 11.4 0 0 0 3.6.57 1 1 0 0 1 1 1V20a1 1 0 0 1-1 1A17 17 0 0 1 3 4a1 1 0 0 1 1-1h3.5a1 1 0 0 1 1 1c0 1.25.2 2.45.57 3.57a1 1 0 0 1-.25 1z"/></svg></div><div><b>Phone</b><span>+61 2 5550 1984</span></div></div>
<div class="info" style="left:448px"><div class="ic"><svg width="22" height="26" viewBox="0 0 22 26" fill="#fff"><path d="M11 0a10 10 0 0 0-10 10c0 7 10 16 10 16s10-9 10-16A10 10 0 0 0 11 0zm0 14a4 4 0 1 1 0-8 4 4 0 0 1 0 8z"/></svg></div><div><b>Address</b><span>123, Lorem ipsum dolor sit<br>Sydney</span></div></div>
<div class="info" style="left:812px"><div class="ic"><svg width="24" height="18" viewBox="0 0 24 18" fill="#fff"><path d="M0 0h24v18H0z" fill="#fff"/><path d="M1 1l11 9 11-9" stroke="#6fb52c" stroke-width="2" fill="none"/></svg></div><div><b>Email</b><span>hello@copperlinegw.com</span></div></div>
<div class="foot-bar"><span>2025 Copyrights - <a>Copperline Groundworks</a> | All Rights Reserved</span><div class="social"><i></i><i class="on"></i><i></i></div></div>

</body>
</html>
```